Infographic comparing two personal financial success strategies

Need an infographic designed comparing typical financial planning advice to my proprietary wealth platform "The Vantage Harbor Method". My system is designed primarily for business owners, professionals and executives who aspire to a work-optional lifestyle. I would like designs that use my websites color palette (www.quillmorecap.com) and include my logo. The final design should highlight the differences between the typical approach and the benefits of the "The Vantage Harbor Method".

Target Market(s)

Business owners, professionals (doctors, lawyers, accoutnants, and business executives

Industry/Entity Type

Financial Service

Font styles to use
Sans Serif

Colors
33a6d7
0455a3
cee9f5

```html
<!DOCTYPE html>
<html lang="en">
<head>
<meta charset="utf-8">
<title>Typical Financial Advice vs The Vantage Harbor Method</title>
<link href="https://fonts.googleapis.com/css2?family=Roboto:wght@400;500;700&display=swap" rel="stylesheet">
<style>
:root{
  --brand-blue:#0455a3;
  --brand-sky:#33a6d7;
  --brand-ice:#cee9f5;
  --panel-grey:#cfcfcf;
  --panel-grey-dark:#bdbdbd;
  --ink:#2b2b2b;
  --badge:#3a3a3a;
  --white:#ffffff;
}
*{box-sizing:border-box;margin:0;padding:0}
html,body{width:794px;height:1200px;overflow:hidden}
body{font-family:'Roboto',Arial,sans-serif;color:var(--ink);background:var(--white);position:relative}
.header{position:absolute;left:0;top:0;width:794px;height:97px;background:var(--white);border-bottom:1px solid #ddd}
.header h1{position:absolute;left:40px;top:28px;font-size:27px;font-weight:500;color:#222}
.brand{position:absolute;left:432px;top:20px;display:flex;align-items:center;gap:12px}
.brand-dot{width:50px;height:50px;border-radius:50%;background:var(--brand-blue)}
.brand-name{font-size:24px;font-weight:700;color:var(--brand-blue);line-height:1;letter-spacing:.3px}
.brand-tag{font-size:15px;color:var(--brand-blue);margin-top:4px;margin-left:58px}
.typical{position:absolute;left:0;top:97px;width:397px;height:1103px;background:linear-gradient(180deg,#f2f2f2,#e4e4e4)}
.method{position:absolute;left:397px;top:97px;width:397px;height:1103px;background:linear-gradient(180deg,#0a5aa6,#0455a3 60%,#064a8e)}
.card{position:absolute;border-radius:4px}
.typical-card{left:26px;width:344px;background:linear-gradient(180deg,var(--panel-grey),var(--panel-grey-dark));padding:9px 12px 8px 50px;font-size:14px;line-height:1.3;box-shadow:0 1px 2px rgba(0,0,0,.2)}
.badge{position:absolute;left:10px;top:8px;width:28px;height:28px;border-radius:50%;background:var(--badge);color:var(--white);font-weight:700;font-size:17px;display:flex;align-items:center;justify-content:center}
.card h2{font-size:14.5px;font-weight:700;line-height:1.3;margin-bottom:6px;margin-top:4px}
.typical-card p{margin-left:-38px}
.sub{padding-left:24px}
.method-card{left:415px;width:363px;background:var(--brand-ice);padding:12px 12px 10px 50px;font-size:14px;line-height:1.3;overflow:hidden}
.method-card .badge{background:#44525e;top:10px}
.method-card h2{color:var(--brand-sky);width:180px}
.method-card p{margin-left:-38px;width:205px}
.method-card .accent{color:var(--brand-sky)}
.method-card .photo{position:absolute;right:0;top:0;width:113px;height:100%}
.method-card .slogan{color:var(--brand-sky);font-weight:700;font-size:15px;line-height:1.35;margin-left:-38px;margin-top:36px;width:220px}
.typical-photo{position:absolute;left:26px;top:922px;width:344px;height:130px;border-radius:4px;background:linear-gradient(160deg,#d9d4cf,#a9a29b 60%,#cfcac4)}
.income-list{left:460px;top:759px;width:318px;height:110px;background:var(--brand-ice);padding:8px 10px 6px 24px;font-size:14px;line-height:1.3}
.income-list .accent{color:var(--brand-sky)}
.income-list ol{padding-left:28px}
.connector{position:absolute;left:0;top:0}
</style>
</head>
<body>
<header class="header">
  <h1>Typical Financial Advice</h1>
  <div class="brand">
    <div class="brand-dot"></div>
    <div>
      <div class="brand-name">QUILLMORE CAPITAL</div>
      <div class="brand-tag" style="margin-left:0">Live life on your terms</div>
    </div>
  </div>
</header>

<section class="typical" aria-label="Typical financial advice"></section>
<section class="method" aria-label="The Vantage Harbor Method"></section>

<div class="card typical-card" style="top:113px;height:85px"><span class="badge">1</span><h2>Make income</h2><p>– Job, Company, Real-Estate, &nbsp;Investments, etc.</p></div>
<div class="card typical-card" style="top:220px;height:98px"><span class="badge">2</span><h2>Pay Taxes</h2><p>– Reduces income<br><span class="sub">a. &nbsp;RRSP</span></p></div>
<div class="card typical-card" style="top:337px;height:105px"><span class="badge">3</span><h2>Pay interest (mortgage, car loan, credit cards, etc.)</h2><p>– Reduces income<br><span class="sub">a. &nbsp;Pay off faster</span></p></div>
<div class="card typical-card" style="top:462px;height:106px"><span class="badge">4</span><h2>Pay for lifestyle (food, shelter, vacations, recreation, education, etc.)</h2><p>– Reduces Income<br><span class="sub">a. &nbsp;Cut back on spending</span></p></div>
<div class="card typical-card" style="top:593px;height:57px"><span class="badge">5</span><h2>Hope for good returns on what you can save</h2></div>
<div class="card typical-card" style="top:671px;height:109px"><span class="badge">6</span><h2>Hope nothing bad happens</h2><p class="sub" style="margin-left:-14px">a. &nbsp;Laid-off, no work, fired, company fails, etc.<br>b. &nbsp;Can’t work for health reason(s)</p></div>
<div class="card typical-card" style="top:799px;height:42px"><span class="badge">7</span><h2>Hope you don’t live too long in retirement</h2></div>
<div class="card typical-card" style="top:860px;height:39px"><span class="badge">8</span><h2>Minimizes future lifestyle and dreams</h2></div>
<div class="typical-photo" role="img" aria-label="Photo of a stressed woman with her head in her hands at a laptop"></div>

<div class="card method-card" style="top:113px;height:131px"><span class="badge">1</span><h2>Cash Flow</h2><p>– Job, Company, Real-Estate, Investments, etc.</p><div class="photo" role="img" aria-label="Photo of a businessman working on a laptop" style="background:linear-gradient(160deg,#e8e8e6,#4a4d55)"></div></div>
<div class="card method-card" style="top:262px;height:174px"><span class="badge">2</span><h2>Cash Flow Maximization</h2><p>– Get the most from your money now, don’t reduce lifestyle<br>a. &nbsp;<span class="accent">Reduce taxes</span> – Flow-through, RRSPs &amp; TFSAs<br>b. &nbsp;<span class="accent">Recapture Interest expense</span> – Use Opportunity Cost</p><div class="photo" role="img" aria-label="Photo of a person relaxing with feet up holding a phone" style="background:linear-gradient(160deg,#c7d6c2,#d9b9a2 60%,#e6ddd3)"></div></div>
<div class="card method-card" style="top:455px;height:134px"><span class="badge">3</span><h2>Cash Flow Protection</h2><p>– Protect &amp; Multiple the uses of your money<br>a. &nbsp;<span class="accent">Protect your income</span><br>b. &nbsp;<span class="accent">Create guaranteed savings</span></p><div class="photo" role="img" aria-label="Photo of a padlock on a stack of banknotes" style="background:linear-gradient(160deg,#f1f1f1,#a89f8c 60%,#7e6a4c)"></div></div>
<div class="card method-card" style="top:610px;height:125px"><span class="badge">4</span><h2>Cash Flow Expansion</h2><p>- Multiple your income streams and increase cash flow now<br>a. &nbsp;<span class="accent">Regularly add new income streams</span></p><div class="photo" role="img" aria-label="Photo of a hand using a calculator over financial charts" style="background:linear-gradient(160deg,#f2f4f6,#9fb7cc)"></div></div>

<svg class="connector" width="794" height="1200" aria-hidden="true"><polyline points="441,735 441,809 460,809" fill="none" stroke="#ffffff" stroke-width="3"/></svg>
<div class="card income-list">
  <div>i. &nbsp;<span class="accent">Dividend and interest paying investments</span></div>
  <ol>
    <li>Direct &amp; In-direct Real-estate</li>
    <li>Private Business ownership</li>
    <li>Company Stocks</li>
    <li>Private Lending</li>
  </ol>
</div>

<div class="card method-card" style="top:894px;height:131px"><span class="badge">5</span><div class="slogan">Work because you want to… not because you have to!</div><div class="photo" role="img" aria-label="Photo of smiling business colleagues at work" style="background:linear-gradient(160deg,#f5f5f5,#6f7c8c)"></div></div>
<div class="card method-card" style="top:1048px;height:130px"><span class="badge">6</span><div class="slogan">BlueSky think your goals, dreams and life!</div><div class="photo" role="img" aria-label="Photo of a woman raising her arms by a lake at sunset" style="background:linear-gradient(180deg,#f3d9a4,#c9a86a 55%,#5e6e4e)"></div></div>
</body>
</html>
```